New Dental Office Needs an Attractive and user friendly Website Designed

I need a website for a new dental office. The Name is Maplecrest Dentistry. I would like a Modern design with a user friendly interface and usability.
I would like a landing page, a page that lists the services we offer: Cosmetic Dentistry, Implants, Dental Hygiene, Emergency Services, Restorations, Dentures
Target Market(s)
Mid to upper class
Industry/Entity Type
Dentistry
Coding
Coded - Design and coding required
Number of Pages Required
1 page
Requirements
Must have
- Landing page that has a scheduling option, Procedures, operating hours, and contact us info
Nice to have
- Appealing design, Soft comforting colors. Easy to navigate page, Modern and professional.

```html
<!DOCTYPE html>
<html lang="en">
<head>
<meta charset="utf-8">
<title>Maplecrest Dentistry</title>
<link href="https://fonts.googleapis.com/css2?family=Marcellus&family=Poppins:wght@400;500&display=swap" rel="stylesheet">
<style>
:root{
  --gold:#f4a81d;
  --gold-dark:#e09612;
  --dark:#262626;
  --ink:#2a2a2a;
  --light:#f6f6f6;
  --white:#fff;
  --serif:"Marcellus", serif;
  --sans:"Poppins", sans-serif;
}
*{box-sizing:border-box;margin:0;padding:0}
html,body{width:1200px;height:4615px;overflow:hidden}
body{position:relative;font-family:var(--sans);color:var(--ink);background:var(--white)}
.abs{position:absolute}
.section{position:absolute;left:0;width:1200px;overflow:hidden}
.photo{position:absolute}
.serif{font-family:var(--serif);font-weight:400}
.btn{position:absolute;display:flex;align-items:center;justify-content:center;gap:10px;background:var(--gold);color:var(--ink);border-radius:22px;font-size:12px;font-weight:500}
.btn svg{width:14px;height:14px}
.gold{color:var(--gold)}
.center{text-align:center;left:0;width:1200px}
.label-line{display:flex;align-items:center;justify-content:center;gap:26px;color:var(--gold);font-size:17px}
.label-line::before,.label-line::after{content:"";width:92px;height:1px;background:var(--gold)}
.logo{font-family:var(--serif);font-size:26px;color:var(--white);white-space:nowrap}

/* hero */
.hero{top:0;height:749px;background:linear-gradient(180deg,#6b6560 0%,#a5948a 35%,#4a4744 70%,#2d2c2b 100%)}
.nav a{position:absolute;top:49px;color:var(--white);font-size:12.5px;text-decoration:none}
.round-arrow{position:absolute;top:356px;width:38px;height:38px;border:1px solid rgba(255,255,255,.7);border-radius:50%;display:flex;align-items:center;justify-content:center}
.dots{position:absolute;display:flex;gap:16px}
.dots span{width:6px;height:6px;border-radius:50%;background:var(--white)}
.dots span.on{background:var(--gold);box-shadow:0 0 0 3px rgba(244,168,29,.35)}

/* about */
.about{top:749px;height:679px;background:var(--dark)}
.about p{position:absolute;left:652px;width:345px;color:#ddd;font-size:10px;line-height:16.5px}

/* services */
.services{top:1428px;height:936px;background:var(--white)}
.card{position:absolute;width:299px;height:281px;overflow:hidden}
.card .cap{position:absolute;left:0;bottom:0;width:100%;padding:0 24px 24px;text-align:center;color:var(--white)}
.card h3{font-family:var(--serif);font-weight:400;font-size:17px;padding-bottom:8px;margin:0 40px 8px;border-bottom:1px solid rgba(255,255,255,.45)}
.card p{font-size:11px;line-height:14px}

/* why */
.why{top:2364px;height:487px;background:var(--dark)}
.why li{position:absolute;left:684px;list-style:none;display:flex;align-items:center;gap:14px;color:#eee;font-size:12px}

/* testimonials */
.testi{top:2851px;height:632px;background:var(--light)}
.tcard{position:absolute;top:192px;width:453px;height:294px;background:var(--white);border:1px solid #ececec;box-shadow:0 0 0 8px #fff,0 2px 14px rgba(0,0,0,.06)}
.tcard .avatar{position:absolute;left:38px;top:70px;width:140px;height:140px;border-radius:50%}
.tcard .stars{position:absolute;left:208px;top:58px;color:var(--gold);font-size:15px;letter-spacing:4px}
.tcard .quote{position:absolute;left:208px;top:90px;width:215px;font-size:10.5px;line-height:17px;color:#333}
.tcard .who{position:absolute;left:208px;top:202px;display:flex;align-items:center;gap:10px}
.tcard .who b{display:block;font-family:var(--serif);font-weight:400;font-size:12.5px}
.tcard .who small{display:block;font-size:9px;color:#555}
.tcard .qmark{position:absolute;right:32px;top:190px;width:54px;height:44px}

/* booking */
.booking{top:3483px;height:591px;background:linear-gradient(90deg,#d8dee2 0%,#eef1f3 45%,#cfd6da 100%)}
.panel{position:absolute;left:630px;top:106px;width:468px;height:382px;background:var(--dark)}
.field{position:absolute;border:1px solid #8a8a8a;color:#ccc;font-size:9.5px;padding:9px 12px}

/* footer */
.footer{top:4074px;height:541px;background:var(--dark);color:var(--white)}
.footer h4{position:absolute;font-weight:400;font-size:15px}
.footer .link{position:absolute;left:256px;font-size:12px;color:#ddd}
.footer .contact{position:absolute;left:867px;display:flex;gap:14px;font-size:11px;color:#ddd;width:220px;line-height:16px}
.footer .contact svg{flex:none}
.social{position:absolute;top:4394px;width:34px;height:34px;border:1.5px solid var(--gold);border-radius:50%}
</style>
</head>
<body>

<section class="section hero">
  <div class="photo" role="img" aria-label="Smiling couple cheek to cheek showing bright white teeth" style="inset:0;background:radial-gradient(ellipse at 40% 25%,#d8c2b0 0%,#9e8576 40%,rgba(60,55,52,0) 75%)"></div>
  <div class="photo" style="inset:0;background:linear-gradient(180deg,rgba(0,0,0,.25) 0%,rgba(0,0,0,0) 20%,rgba(0,0,0,.25) 45%,rgba(0,0,0,.55) 100%)"></div>
  <nav class="nav">
    <a style="left:118px">Home</a>
    <a style="left:188px">About</a>
    <a style="left:258px">Services</a>
    <a style="left:343px">Testimonials</a>
    <a style="left:754px">Blogs</a>
    <a style="left:824px">Contact</a>
  </nav>
  <div class="abs logo" style="left:0;width:1200px;text-align:center;top:40px">Maplecrest Dentistry</div>
  <div class="btn" style="left:904px;top:36px;width:181px;height:42px;font-size:11.5px">
    <svg viewBox="0 0 24 24"><path d="M6.6 10.8a15 15 0 0 0 6.6 6.6l2.2-2.2a1 1 0 0 1 1-.25 11.4 11.4 0 0 0 3.6.57 1 1 0 0 1 1 1V20a1 1 0 0 1-1 1A17 17 0 0 1 3 4a1 1 0 0 1 1-1h3.5a1 1 0 0 1 1 1c0 1.25.2 2.45.57 3.57a1 1 0 0 1-.25 1z" fill="#2a2a2a"/></svg>
    Book Appointment
  </div>
  <div class="round-arrow" style="left:74px"><svg width="12" height="12" viewBox="0 0 12 12"><path d="M8 1 3 6l5 5" stroke="#fff" fill="none"/></svg></div>
  <div class="round-arrow" style="left:1088px"><svg width="12" height="12" viewBox="0 0 12 12"><path d="m4 1 5 5-5 5" stroke="#f4a81d" fill="none"/></svg></div>
  <div class="abs center gold" style="top:344px;font-size:21px">Your Smile Starts Here</div>
  <h1 class="abs center serif" style="top:380px;color:#fff;font-size:44px;line-height:54px">Modern Dental Care With Comfort,<br>Compassion, &amp; Confidence.</h1>
  <div class="btn" style="left:510px;top:516px;width:180px;height:41px">
    <svg viewBox="0 0 24 24"><path d="M6.6 10.8a15 15 0 0 0 6.6 6.6l2.2-2.2a1 1 0 0 1 1-.25 11.4 11.4 0 0 0 3.6.57 1 1 0 0 1 1 1V20a1 1 0 0 1-1 1A17 17 0 0 1 3 4a1 1 0 0 1 1-1h3.5a1 1 0 0 1 1 1c0 1.25.2 2.45.57 3.57a1 1 0 0 1-.25 1z" fill="#2a2a2a"/></svg>
    Book Appointment
  </div>
  <div class="dots" style="left:553px;top:660px"><span></span><span></span><span class="on"></span><span></span><span></span></div>
</section>

<section class="section about">
  <div class="abs center label-line" style="top:78px">Welcome to Maplecrest</div>
  <h2 class="abs center serif" style="top:103px;color:#fff;font-size:42px;line-height:44px">We Provide Best Dental<br>Services</h2>
  <div class="abs" style="left:197px;top:200px;width:158px;height:233px;border:1.5px solid var(--gold)"></div>
  <div class="photo" role="img" aria-label="Close-up of a dentist using a handpiece and mirror on a patient's teeth" style="left:210px;top:213px;width:309px;height:297px;background:linear-gradient(135deg,#c99a8a 0%,#e3d3cf 45%,#8fb6d9 100%)"></div>
  <div class="abs" style="left:392px;top:367px;width:231px;height:222px;background:#111;padding:8px">
    <div role="img" aria-label="Two smiling dentists in white coats standing in a clinic" style="width:100%;height:100%;background:linear-gradient(180deg,#e9ecee 0%,#cfd6db 100%);border:2px solid #fff"></div>
  </div>
  <p style="top:238px">Compassionate Dentistry With A Modern Touch Maplecrest Dentistry Was Founded On The Principles Of Personalized Care And Clinical Excellence. Our Highly Trained Team Blends The Latest In Dental Innovation With A Friendly, Welcoming Environment Designed To Put You At Ease. Whether You're Here For A Routine Visit Or Specialized Treatment, Our Focus Is Always Your Health, Comfort, And Satisfaction.</p>
  <p style="top:370px">Our Dentists Bring Years Of Experience Across General, Cosmetic, And Restorative Dentistry, And They Are Continuously Learning To Stay Ahead Of Advancements In Dental Science And Patient Care. At Maplecrest Dentistry, You're Not Just A Patient — You're Part Of Our Dental Family.</p>
  <div class="btn" style="left:652px;top:481px;width:201px;height:37px;font-size:11px">Read More About Us
    <svg viewBox="0 0 14 14"><path d="M2 7h10M8 3l4 4-4 4" stroke="#2a2a2a" fill="none" stroke-width="1.4"/></svg></div>
</section>

<section class="section services">
  <h2 class="abs center serif" style="top:62px;font-size:40px">What Service Provide</h2>
  <div class="abs center label-line" style="top:120px;font-size:14px">Our Services</div>

  <div class="card" style="left:131px;top:173px">
    <div class="photo" role="img" aria-label="Close-up of a bright white smile" style="inset:0;background:linear-gradient(180deg,#b24a4a 0%,#e8dcd6 40%,#5a2a2a 75%,#1a1a1a 100%)"></div>
    <div class="cap"><h3>Cosmetic Dentistry</h3><p>Brighten, straighten, and enhance your smile.</p></div>
  </div>
  <div class="card" style="left:451px;top:173px">
    <div class="photo" role="img" aria-label="Dental implant model with crown" style="inset:0;background:linear-gradient(180deg,#6a6a6a 0%,#2a2a2a 35%,#b58520 75%,#f4a81d 100%)"></div>
    <div class="cap" style="bottom:auto;top:106px"><h3>Dental Implants</h3><p>Permanent solutions for missing teeth.</p></div>
    <div class="abs" style="left:109px;top:246px;width:80px;height:80px;border-radius:50%;background:var(--gold-dark)"></div>
    <svg class="abs" style="left:141px;top:256px" width="16" height="16" viewBox="0 0 14 14"><path d="M2 7h10M8 3l4 4-4 4" stroke="#fff" fill="none" stroke-width="1.2"/></svg>
  </div>
  <div class="card" style="left:772px;top:173px">
    <div class="photo" role="img" aria-label="Smiling woman holding a toothbrush" style="inset:0;background:linear-gradient(180deg,#8a5a48 0%,#d9b7a6 40%,#4a3a34 75%,#1a1a1a 100%)"></div>
    <div class="cap"><h3>Dental Hygiene</h3><p>Preventive care to keep your smile healthy.</p></div>
  </div>
  <div class="card" style="left:131px;top:474px">
    <div class="photo" role="img" aria-label="Dentist treating a patient holding her cheek in pain" style="inset:0;background:linear-gradient(180deg,#c9c9c9 0%,#a88a7a 45%,#3a3232 80%,#1a1a1a 100%)"></div>
    <div class="cap"><h3>Emergency Services</h3><p>Urgent care when you need it most.</p></div>
  </div>
  <div class="card" style="left:451px;top:474px">
    <div class="photo" role="img" aria-label="Teeth before and after restoration" style="inset:0;background:linear-gradient(180deg,#b85858 0%,#d9c9a8 40%,#3a2a22 75%,#1a1a1a 100%)"></div>
    <div class="cap"><h3>Restorations</h3><p>Fillings, crowns, and bridges to repair your smile.</p></div>
  </div>
  <div class="card" style="left:772px;top:474px">
    <div class="photo" role="img" aria-label="Full denture model on grey background" style="inset:0;background:linear-gradient(180deg,#5a5a60 0%,#b04848 40%,#4a4a50 70%,#1a1a1a 100%)"></div>
    <div class="cap"><h3>Dentures</h3><p>Full or partial dentures for restored functionality.</p></div>
  </div>

  <div class="btn" style="left:516px;top:807px;width:168px;height:40px;font-size:11.5px">View All Services
    <svg viewBox="0 0 14 14"><path d="M2 7h10M8 3l4 4-4 4" stroke="#2a2a2a" fill="none" stroke-width="1.4"/></svg></div>
</section>

<section class="section why">
  <div class="photo" role="img" aria-label="Dentist examining a smiling male patient in the chair" style="left:0;top:0;width:600px;height:487px;background:linear-gradient(135deg,#e6eaec 0%,#cfd8de 40%,#7d9bb8 75%,#b7c8d6 100%)"></div>
  <div class="abs gold" style="left:684px;top:98px;font-size:14px;display:flex;align-items:center;gap:12px">Maplecrest Dentistry <span style="width:40px;height:1px;background:var(--gold)"></span></div>
  <h2 class="abs serif" style="left:684px;top:122px;color:#fff;font-size:32px">Why Choose Us</h2>
  <ul>
    <li style="top:203px"><svg width="12" height="12" viewBox="0 0 14 14"><path d="M2 7h10M8 3l4 4-4 4" stroke="#f4a81d" fill="none" stroke-width="1.4"/></svg>Modern, Comfortable Office Environment</li>
    <li style="top:243px"><svg width="12" height="12" viewBox="0 0 14 14"><path d="M2 7h10M8 3l4 4-4 4" stroke="#f4a81d" fill="none" stroke-width="1.4"/></svg>Friendly, Professional Dental Team</li>
    <li style="top:282px"><svg width="12" height="12" viewBox="0 0 14 14"><path d="M2 7h10M8 3l4 4-4 4" stroke="#f4a81d" fill="none" stroke-width="1.4"/></svg>Latest Technology and Equipment</li>
    <li style="top:321px"><svg width="12" height="12" viewBox="0 0 14 14"><path d="M2 7h10M8 3l4 4-4 4" stroke="#f4a81d" fill="none" stroke-width="1.4"/></svg>Personalized Care for Every Patient</li>
    <li style="top:359px"><svg width="12" height="12" viewBox="0 0 14 14"><path d="M2 7h10M8 3l4 4-4 4" stroke="#f4a81d" fill="none" stroke-width="1.4"/></svg>Convenient Scheduling &amp; Emergency Support</li>
  </ul>
</section>

<section class="section testi">
  <h2 class="abs center serif" style="top:78px;font-size:40px">What Our Client Says</h2>
  <div class="abs center label-line" style="top:131px;font-size:14px">Testimonials</div>
  <div class="round-arrow" style="left:74px;top:320px;border-color:#999"><svg width="12" height="12" viewBox="0 0 12 12"><path d="M8 1 3 6l5 5" stroke="#555" fill="none"/></svg></div>
  <div class="round-arrow" style="left:1088px;top:320px;border-color:var(--gold)"><svg width="12" height="12" viewBox="0 0 12 12"><path d="m4 1 5 5-5 5" stroke="#f4a81d" fill="none"/></svg></div>

  <div class="tcard" style="left:134px">
    <div class="avatar" role="img" aria-label="Portrait of a smiling young woman with glasses" style="background:linear-gradient(180deg,#f3dfb0 0%,#f0d49a 60%,#8fb0d6 100%)"></div>
    <div class="stars">★★★★★</div>
    <div class="quote">Maplecrest Dentistry made me feel completely at ease. They're professional, gentle, and incredibly knowledgeable. Highly recommend!</div>
    <div class="who"><span style="width:18px;height:18px;border-radius:50%;background:#ddd"></span><span><b>Clara M.</b><small>Real Client</small></span></div>
    <svg class="qmark" viewBox="0 0 54 44"><path d="M4 6h18v18c0 10-6 16-16 18l-1-6c6-1 9-5 9-10H4z M30 6h18v18c0 10-6 16-16 18l-1-6c6-1 9-5 9-10H30z" fill="#f6d58f"/></svg>
  </div>
  <div class="tcard" style="left:614px">
    <div class="avatar" role="img" aria-label="Portrait of a smiling young man in a light shirt" style="background:linear-gradient(180deg,#f3dfb0 0%,#f0d49a 60%,#dfe6ee 100%)"></div>
    <div class="stars">★★★★★</div>
    <div class="quote">Maplecrest Dentistry made me feel completely at ease. They're professional, gentle, and incredibly knowledgeable. Highly recommend!</div>
    <div class="who"><span style="width:18px;height:18px;border-radius:50%;background:#ddd"></span><span><b>Clara M.</b><small>Real Client</small></span></div>
    <svg class="qmark" viewBox="0 0 54 44"><path d="M4 6h18v18c0 10-6 16-16 18l-1-6c6-1 9-5 9-10H4z M30 6h18v18c0 10-6 16-16 18l-1-6c6-1 9-5 9-10H30z" fill="#f6d58f"/></svg>
  </div>

  <div class="dots" style="left:553px;top:545px"><span style="background:#ccc"></span><span style="background:#ccc"></span><span class="on"></span><span style="background:#ccc"></span><span style="background:#ccc"></span></div>
</section>

<section class="section booking">
  <div class="photo" role="img" aria-label="Smiling female and male dentists in white coats in a bright clinic" style="left:0;top:0;width:640px;height:591px;background:linear-gradient(90deg,rgba(230,215,200,.6) 0%,rgba(245,245,245,.5) 40%,rgba(200,210,218,.4) 100%)"></div>
  <div class="panel">
    <h2 class="abs serif" style="left:0;width:468px;text-align:center;top:40px;color:#fff;font-size:26px">Book Your Appointment</h2>
    <div class="abs label-line" style="left:0;width:468px;top:78px;font-size:14px">Contact Us</div>
    <div class="field" style="left:56px;top:122px;width:172px;height:31px">First Name *</div>
    <div class="field" style="left:242px;top:122px;width:172px;height:31px">Last Name *</div>
    <div class="field" style="left:56px;top:168px;width:172px;height:31px">Email Address *</div>
    <div class="field" style="left:242px;top:168px;width:172px;height:31px">Phone No. *</div>
    <div class="field" style="left:56px;top:213px;width:358px;height:62px">Your Message *</div>
    <div class="btn" style="left:147px;top:288px;width:174px;height:39px;font-size:11.5px">Get In Touch
      <svg viewBox="0 0 14 14"><path d="M2 7h10M8 3l4 4-4 4" stroke="#2a2a2a" fill="none" stroke-width="1.4"/></svg></div>
  </div>
</section>

<footer class="section footer">
  <h4 style="left:256px;top:146px">Quick Links</h4>
  <div class="link" style="top:182px">Home</div>
  <div class="link" style="top:208px">About Us</div>
  <div class="link" style="top:234px">Services</div>
  <div class="link" style="top:260px">Blog</div>
  <div class="link" style="top:286px">Contact Us</div>

  <div class="abs logo" style="left:0;width:1200px;text-align:center;top:132px">Maplecrest Dentistry</div>
  <div class="abs" style="left:442px;top:258px;width:316px;height:24px;border-bottom:1px solid #777;font-size:10px;color:#aaa">Email Address*</div>
  <svg class="abs" style="left:738px;top:258px" width="16" height="16" viewBox="0 0 16 16"><path d="M1 8 15 1 11 15 8 9z" fill="#fff"/></svg>

  <h4 style="left:867px;top:146px">Contact Us</h4>
  <div class="contact" style="top:188px"><svg width="15" height="15" viewBox="0 0 24 24"><path d="M6.6 10.8a15 15 0 0 0 6.6 6.6l2.2-2.2a1 1 0 0 1 1-.25 11.4 11.4 0 0 0 3.6.57 1 1 0 0 1 1 1V20a1 1 0 0 1-1 1A17 17 0 0 1 3 4a1 1 0 0 1 1-1h3.5a1 1 0 0 1 1 1c0 1.25.2 2.45.57 3.57a1 1 0 0 1-.25 1z" fill="none" stroke="#f4a81d" stroke-width="1.6"/></svg>(555) 214-3870</div>
  <div class="contact" style="top:236px"><svg width="15" height="15" viewBox="0 0 24 24"><rect x="2" y="5" width="20" height="14" fill="none" stroke="#f4a81d" stroke-width="1.6"/><path d="m2 6 10 7 10-7" fill="none" stroke="#f4a81d" stroke-width="1.6"/></svg>hello@maplecrestdental.com</div>
  <div class="contact" style="top:284px"><svg width="15" height="15" viewBox="0 0 24 24"><path d="M12 22s7-7 7-12a7 7 0 0 0-14 0c0 5 7 12 7 12z" fill="none" stroke="#f4a81d" stroke-width="1.6"/><circle cx="12" cy="10" r="2.5" fill="none" stroke="#f4a81d" stroke-width="1.6"/></svg>48 Orchard Ave, 2nd Floor, Maplecrest, NY</div>
  <div class="contact" style="top:332px"><svg width="15" height="15" viewBox="0 0 24 24"><circle cx="12" cy="12" r="9" fill="none" stroke="#f4a81d" stroke-width="1.6"/><path d="M12 7v5l3 2" fill="none" stroke="#f4a81d" stroke-width="1.6"/></svg>Mon – Fri 8am – 6pm, Sat 9am – 2pm</div>

  <div class="abs center" style="top:486px;font-size:9.5px;color:#aaa">Copyright © 2025 Maplecrest Dentistry &nbsp;|&nbsp; Privacy Policy &nbsp;|&nbsp; Terms &amp; Condition</div>
</footer>
<div class="social" style="left:502px" aria-label="Social profile"></div>
<div class="social" style="left:553px" aria-label="Social profile"></div>
<div class="social" style="left:604px" aria-label="Social profile"></div>
<div class="social" style="left:655px" aria-label="Social profile"></div>

</body>
</html>
```